Larchfield Shopping Centre main sign re-design project

We would like to refresh the look of the main sign we have on the corner of a block of shops to make it more contemproary and vibrant.

A picture of the existing sign which reads Larchfield Shopping Centre can be found in attached PDF and at the following URL.

http://www.quentorprop.example.nz/~/media/Listings/Region%20One/Sample%20Town/Sample%20Town%20CBD/418207/Images/418207_1.ashx?bc=Gainsboro&as=1&h=550&w=980&ma=1

Larchfield Shopping Centre is also know locally as Larchfield Plaza, but the key word is Larchfield.

The existing signage has a flower/clover pattern on it which I think was just added to create a bit of interest. The building is located in a town surrounded by farm land.

I do quite like the organic feel of plant leaves or certain flowers - preferably New Zealand native plants for instance - the Kowhai flower or leaf block, pohutukawa, or kaka beak - reference images can be found with google image search

Geometric patterns could also be an option.

Once again the imagery is only to soften the sign and add some interest.
Updates

                                        Additional images of existing signage added

Project Deadline Extended
Reason: Closing date extended to allow for fact that lead up to Christmas is a busy time of year for many people.

Target Market(s)

The target audience is premium shopper

Industry/Entity Type

Building

Requirements
Must have
• Must have the words: Larchfield Shopping Centre.
The big M is not essential, and I would rather the emphasis was on the word Larchfield.
Should not have
• Should not be brown. We want the sign to feel more contemporary, but not too hard. The current pale brown feels too soft in comparison with the look of the building.

```html
<!DOCTYPE html>
<html lang="en">
<head>
<meta charset="utf-8">
<title>Larchfield Shopping Centre – Main Sign</title>
<link rel="stylesheet" href="https://fonts.googleapis.com/css2?family=Cormorant+Garamond:wght@500&display=swap">
<style>
  :root {
    --sign-red: #cb3800;
    --sign-amber: #e07000;
    --sign-white: #ffffff;
    --page-bg: #ffffff;
  }
  html, body {
    margin: 0;
    padding: 0;
    overflow: hidden;
    background: var(--page-bg);
  }
  .canvas {
    position: relative;
    width: 1200px;
    height: 1000px;
    overflow: hidden;
    background: var(--page-bg);
  }
  .sign-panel {
    position: absolute;
    left: 457px;
    top: 24px;
    width: 551px;
    height: 933px;
    background: var(--sign-red);
    overflow: hidden;
  }
  .sign-stripes {
    position: absolute;
    inset: 0;
    width: 100%;
    height: 100%;
  }
  .sign-stripes polygon { fill: var(--sign-amber); }
  .brand-square {
    position: absolute;
    left: 108px;
    top: 143px;
    width: 341px;
    height: 399px;
    background: var(--sign-white);
  }
  .brand-name,
  .brand-descriptor {
    position: absolute;
    left: 0;
    width: 100%;
    margin: 0;
    text-align: center;
    color: var(--sign-white);
    font-family: "Cormorant Garamond", Georgia, serif;
    font-weight: 500;
    line-height: 1;
  }
  .brand-name {
    top: 560px;
    font-size: 54px;
    letter-spacing: 0.02em;
  }
  .brand-descriptor {
    top: 680px;
    font-size: 46px;
    letter-spacing: 0.14em;
    line-height: 48px;
  }
</style>
</head>
<body>
<div class="canvas">
  <section class="sign-panel" aria-label="Larchfield Shopping Centre sign">
    <svg class="sign-stripes" viewBox="0 0 551 933" preserveAspectRatio="none" aria-hidden="true">
      <polygon points="348,0 451,0 551,64 551,159"/>
      <polygon points="0,714 0,781 193,933 343,933"/>
    </svg>
    <div class="brand-square" aria-hidden="true"></div>
    <h1 class="brand-name">LARCHFIELD</h1>
    <p class="brand-descriptor">SHOPPING<br>CENTRE</p>
  </section>
</div>
</body>
</html>
```